Kartonbox
Zielgruppe
Ich bin Spielautor und arbeite für keine Firma. Zielgruppe: Spieler für Erwachsene und Kinder ab 9 Jahren (Brett- und Kartenspieler).
Aufgabenstellung
Es muss eine Kartonbox sein die Platz hat für 56 Spielkarten und einer dünnen Anleitung. Das Kartendesign besteht bereits. Dss heisst das Verpackungsdesign muss an das Kartendesign angepasst werden. Das Spiel heisst 'Das Reich der Flügel' und es geht wie der Name sagt um Vögel die hauptsächlich in der Schweiz vorkommen. Verpackungssmasse gemäss Stanzrisszeichnung im Anhang. Es müssen bestimmte Piktogramme wie Alter, Anzahl Spieler, Dauer, CE Zertifizierung etc. platziert werden. EAN Code ist keiner vorgesehen. Auf der Rückseite sollte noch ein Foto des Autors sowie eine kurze Spielbeschreibung platziert werden sowie die Bezugsadresse (ca. 4 Zeilen).

```html
<!DOCTYPE html>
<html lang="de">
<head>
<meta charset="utf-8">
<title>Das Reich der Flügel – Kartonbox</title>
<link rel="stylesheet" href="https://fonts.googleapis.com/css2?family=Courgette&family=Dancing+Script:wght@500&family=Figtree:wght@400&display=swap">
<style>
  :root {
    --stage: #ececea;
    --paper: #d7d4a6;
    --paper-light: #e2dfbb;
    --paper-deep: #c9c58d;
    --ink: #6a3b40;
    --ribbon: #fbfaf6;
    --ribbon-edge: #c8c0a6;
    --badge: #efebe6;
    --badge-edge: #d3ccc2;
    --mark: #a99f98;
    --tile-rose: #d8b4b2;
    --tile-mint: #a8d5c4;
    --tile-lilac: #b2b7dc;
  }
  * { box-sizing: border-box; margin: 0; padding: 0; }
  html, body { width: 1200px; height: 840px; overflow: hidden; background: var(--stage); }
  .canvas { position: relative; width: 1200px; height: 840px; }

  .panel {
    position: absolute;
    background:
      radial-gradient(ellipse at 30% 25%, var(--paper-light) 0%, transparent 55%),
      radial-gradient(ellipse at 70% 75%, var(--paper-deep) 0%, transparent 60%),
      var(--paper);
  }
  .flap-top   { left: 194px; top: 64px;  width: 378px; height: 157px; }
  .flap-left  { left: 38px;  top: 220px; width: 157px; height: 513px; }
  .front      { left: 195px; top: 220px; width: 378px; height: 513px; }
  .flap-right { left: 573px; top: 220px; width: 159px; height: 513px; }
  .back       { left: 785px; top: 220px; width: 379px; height: 514px; }

  .ribbon { position: absolute; left: 0; width: 378px; height: 88px; }
  .ribbon svg { position: absolute; inset: 0; }
  .ribbon-title {
    position: absolute; left: 0; right: 0; top: 22px;
    text-align: center;
    font-family: "Courgette", cursive;
    font-weight: 400;
    font-size: 36px; color: var(--ink);
    transform: rotate(-3deg);
  }
  .flap-top .ribbon { top: 32px; transform: rotate(180deg); }
  .front .ribbon { top: 334px; z-index: 2; }

  .badge {
    position: absolute; left: 23px; width: 66px; height: 66px;
    border-radius: 50%;
    background: radial-gradient(circle at 40% 35%, #fff 0%, var(--badge) 60%, #ddd6cf 100%);
    border: 2px solid var(--badge-edge);
    box-shadow: 0 2px 3px rgba(90,70,50,.25);
    text-align: center; color: var(--ink);
    font-family: "Dancing Script", cursive;
    padding-top: 9px;
  }
  .badge-value { display: block; font-size: 16px; line-height: 16px; }
  .badge-label { display: block; font-size: 13px; line-height: 14px; }
  .badge-players  { top: 12px; }
  .badge-age      { top: 86px; }
  .badge-duration { top: 158px; }
  .badge-cert     { top: 235px; padding-top: 12px; }
  .cert-mark {
    display: block; margin: 0 auto; width: 32px; height: 22px;
    border-radius: 4px; background: var(--mark);
  }
  .cert-label { display: block; margin-top: 4px; font-size: 10px; line-height: 11px; }

  .hero-owl {
    position: absolute; left: 87px; top: 23px; width: 262px; height: 340px;
    border-radius: 45% 45% 30% 30%;
    background: radial-gradient(ellipse at 50% 40%, #ece0dc 0%, #9b7468 45%, #6e4a40 80%, transparent 100%);
  }
  .tiles { position: absolute; left: 0; top: 403px; width: 378px; height: 110px; display: flex; }
  .tile { flex: 1; }
  .tile-rose  { background: linear-gradient(160deg, var(--tile-rose), #e3c9c6); }
  .tile-mint  { background: linear-gradient(160deg, var(--tile-mint), #c2e3d6); }
  .tile-lilac { background: linear-gradient(160deg, var(--tile-lilac), #c8cce6); }

  .emblem {
    position: absolute; top: 211px; width: 84px; height: 84px; border-radius: 50%;
    border: 1px solid #c4bf8d;
    background: radial-gradient(circle, #c9c38c 0%, #d3cf9f 55%, transparent 70%);
  }
  .flap-left .emblem  { left: 37px; }
  .flap-right .emblem { left: 38px; }

  .author-photo {
    position: absolute; left: 39px; top: 20px; width: 152px; height: 152px;
    border-radius: 50%;
    border: 4px solid #cfc9b4;
    background: radial-gradient(circle at 50% 40%, #d9d7d2 0%, #8d8a86 50%, #3c3a3a 100%);
  }
  .authors {
    position: absolute; left: 56px; top: 178px;
    font-family: "Figtree", sans-serif; font-size: 11px; line-height: 13.5px; color: var(--ink);
  }
  .facts {
    position: absolute; left: 213px; top: 22px;
    font-family: "Figtree", sans-serif; font-size: 17px; line-height: 22.5px; color: var(--ink);
  }
  .facts p + p { margin-top: 4px; }
  .description {
    position: absolute; left: 28px; top: 248px; width: 330px;
    font-family: "Figtree", sans-serif; font-size: 14px; line-height: 17.75px;
    letter-spacing: 0.2px;
    color: var(--ink);
  }
  .description .line {
    display: block; white-space: nowrap;
    text-align: justify; text-align-last: justify;
  }
  .description .line-last { text-align: left; text-align-last: left; }
  .supply-address {
    position: absolute; left: 28px; top: 466px;
    font-family: "Figtree", sans-serif; font-size: 14px; letter-spacing: 0.2px; color: var(--ink);
  }
</style>
</head>
<body>
<main class="canvas">

  <section class="panel flap-top">
    <div class="ribbon">
      <svg viewBox="0 0 378 88" width="378" height="88" aria-hidden="true">
        <path d="M2,14 C120,34 250,-2 376,12 L376,76 C250,62 120,96 2,80 Z" fill="var(--ribbon)" stroke="var(--ribbon-edge)" stroke-width="5"/>
      </svg>
      <div class="ribbon-title">Das Reich der Flügel</div>
    </div>
  </section>

  <section class="panel flap-left">
    <div class="emblem" role="img" aria-label="Dezente Vogelsilhouetten im Kreis"></div>
  </section>

  <section class="panel front">
    <div class="hero-owl" role="img" aria-label="Aquarell eines Raufusskauzes auf einem Ast"></div>

    <div class="badge badge-players"><span class="badge-value">2-5</span><span class="badge-label">Personen</span></div>
    <div class="badge badge-age"><span class="badge-value">9+</span><span class="badge-label">Jahre</span></div>
    <div class="badge badge-duration"><span class="badge-value">10-20</span><span class="badge-label">Minuten</span></div>
    <div class="badge badge-cert">
      <span class="cert-mark" role="img" aria-label="Zertifizierungszeichen"></span>
      <span class="cert-label">zertifiziert</span>
    </div>

    <div class="ribbon">
      <svg viewBox="0 0 378 88" width="378" height="88" aria-hidden="true">
        <path d="M2,14 C120,34 250,-2 376,12 L376,76 C250,62 120,96 2,80 Z" fill="var(--ribbon)" stroke="var(--ribbon-edge)" stroke-width="5"/>
      </svg>
      <h1 class="ribbon-title">Das Reich der Flügel</h1>
    </div>

    <div class="tiles">
      <div class="tile tile-rose" role="img" aria-label="Aquarell einer Weidenmeise auf einem Ast"></div>
      <div class="tile tile-mint" role="img" aria-label="Aquarell einer Elster auf einem Pfahl"></div>
      <div class="tile tile-lilac" role="img" aria-label="Aquarell einer Löffelente"></div>
    </div>
  </section>

  <section class="panel flap-right">
    <div class="emblem" role="img" aria-label="Dezente Vogelsilhouetten im Kreis"></div>
  </section>

  <section class="panel back">
    <div class="author-photo" role="img" aria-label="Foto der beiden Spielautoren"></div>
    <p class="authors">AUTOREN:<br>Konrad Wyss<br>Mateo Lucas Ferreira</p>
    <div class="facts">
      <p>2 - 5 Personen<br>Alter 9+<br>Dauer 10 - 20 Min.</p>
      <p>Anleitung:<br>DE, FR, IT, EN</p>
      <p>Mit Regel für<br>SOLO Spiel,<br>Dauer 5 – 10 Min.</p>
    </div>
    <p class="description">
      <span class="line">Ein unterhaltsames und lehrreiches Kartenspiel</span>
      <span class="line">über Schweizer Vögel. Die Spieler sammeln Vögel,</span>
      <span class="line">Enten und Eulen, um Dreiergruppen von Karten zu</span>
      <span class="line">bilden, die je nach Kartentyp mehr oder weniger</span>
      <span class="line">Punkte ergeben. Kartengruppen mit Vögeln der</span>
      <span class="line">gleichen Landschaftsart geben zusätzliche Punkte.</span>
      <span class="line">Das Spiel kann aber auch überraschend enden,</span>
      <span class="line">wenn ein Spieler die erforderliche Anzahl Nestkar-</span>
      <span class="line">ten auf seiner Hand hat. Deshalb werden die Spie-</span>
      <span class="line">ler manchmal vor knifflige Entscheidungen gestellt,</span>
      <span class="line">wobei das Glück auch mitspielt. Alle Vögel sind</span>
      <span class="line line-last">handgezeichnet.</span>
    </p>
    <p class="supply-address">Bezugsadresse Bezugugsadresse Bezugsadresse</p>
  </section>

</main>
</body>
</html>
```